Trading company needs a non alcoholic beer Can design

We KLV are trading company , food Distributors in Africa -RD Congo/Kinshasa .We want to do a Private label non alcoholic beer 500ml can and need a design for this Project .
the Brand Name is : RIVO BREW
We want it to be similar NOT a copy of Halvenor 0.0% can ( picture
attached ) as we want to respect the intellectual properties .so we prefer to use the same colors but more elegant ,modern style .
thanks.
THE DESIGN MUST STATE ITS A NON ALCOHOLIC BEER
PLZ SEARCH FOR HALVENOR 0.0% MALT DRINK YOU WILL FIND 2 DESIGNS OLD AND NEW WE NEED SOMTHING SIMILAR TO THESE DESIGNS ,KINDLY USE SAME COLORS AND THE 0.0% SHOULD BE IN THE MIDDLE OF THE CAN .
Target Market(s)
THE PRODUCT WILL BE SOLD IN THE SUPERMASRKTS / MODERN TRADE
Look and feel
Each slider illustrates characteristics of the customer's brand and the style your logo design should communicate.

```html
<!DOCTYPE html>
<html lang="en">
<head>
<meta charset="utf-8">
<title>RIVO BREW Premium 0.0% Can Label</title>
<link rel="stylesheet" href="https://fonts.googleapis.com/css2?family=Playfair+Display:wght@500&family=Parisienne&family=Montserrat:wght@600;700&family=Russo+One&display=swap">
<style>
  :root {
    --backdrop: #e6e6e6;
    --silver: #ececec;
    --silver-shade: #d2d2d2;
    --red: #c8341c;
    --red-deep: #a8220f;
    --red-light: #e0553a;
    --blue: #2f55a8;
    --blue-deep: #1f3f8a;
    --gold: #d4aa3a;
    --white: #ffffff;
  }
  * { box-sizing: border-box; margin: 0; padding: 0; }
  html, body { width: 960px; height: 1200px; overflow: hidden; background: var(--backdrop); }
  .canvas { position: relative; width: 960px; height: 1200px; }

  .label {
    position: absolute; left: 300px; top: 170px; width: 360px; height: 860px;
    background: var(--silver); overflow: hidden; border-radius: 4px;
  }
  .side-pattern {
    position: absolute; top: 0; bottom: 0; width: 42px;
    background: linear-gradient(180deg, var(--silver), var(--silver-shade), var(--silver));
  }
  .side-pattern.left { left: 0; }
  .side-pattern.right { right: 0; }
  .red-panel {
    position: absolute; left: 42px; right: 42px; top: 0; bottom: 0;
    background: linear-gradient(180deg, var(--red-light) 0%, var(--red) 35%, var(--red-deep) 100%);
  }

  .brand-frame { position: absolute; left: 0; top: 176px; width: 360px; height: 220px; }
  .brand-badge {
    position: absolute; left: 143px; top: 130px; width: 74px; height: 74px; border-radius: 50%;
    background: var(--blue); border: 3px solid var(--white);
    display: flex; align-items: center; justify-content: center;
  }
  .brand-badge span {
    font-family: "Montserrat", sans-serif; font-weight: 700; font-size: 10px;
    color: var(--white); letter-spacing: 0.3px; white-space: nowrap;
  }
  .laurel {
    position: absolute; top: 244px; width: 18px; height: 70px; border-radius: 40% 40% 50% 50%;
    background: linear-gradient(180deg, var(--gold), #b58a22);
  }
  .laurel.left { left: 44px; }
  .laurel.right { right: 44px; }
  .flourish {
    position: absolute; left: 120px; top: 226px; width: 120px; height: 8px; border-radius: 4px;
    background: linear-gradient(90deg, transparent, var(--gold), transparent);
  }
  .brand-name {
    position: absolute; left: 0; right: 0; top: 248px; text-align: center;
    font-family: "Playfair Display", serif; font-weight: 500; font-size: 37px;
    color: var(--white); letter-spacing: -0.5px; line-height: 1; white-space: nowrap;
  }
  .brand-sub {
    position: absolute; left: 0; right: 0; top: 296px; text-align: center;
    font-family: "Parisienne", cursive; font-size: 24px; color: var(--white); line-height: 1;
  }

  .alc-band { position: absolute; left: 42px; top: 390px; width: 276px; height: 210px; }
  .alc-mark {
    position: absolute; left: 42px; width: 276px; top: 428px;
    display: flex; justify-content: center; align-items: flex-start; gap: 6px;
    color: var(--white); font-family: "Russo One", sans-serif;
    transform: skewY(-8deg);
  }
  .alc-figure { font-size: 100px; line-height: 1; letter-spacing: -3px; }
  .alc-side { display: flex; flex-direction: column; align-items: flex-start; padding-top: 2px; }
  .alc-percent { font-size: 50px; line-height: 1; }
  .alc-unit { font-size: 22px; line-height: 1; margin-top: 2px; }

  .variant { position: absolute; left: 0; right: 0; top: 652px; text-align: center; color: var(--white); font-family: "Montserrat", sans-serif; }
  .variant-tier { font-weight: 700; font-size: 17px; letter-spacing: 1.5px; line-height: 1.1; }
  .variant-name { font-weight: 600; font-size: 31px; letter-spacing: 0.5px; line-height: 1.05; }
  .variant-type { font-weight: 600; font-size: 10.5px; letter-spacing: 0.5px; line-height: 1.3; }
  .variant-rule { width: 66px; height: 2px; background: var(--white); margin: 6px auto 0; }

  .volume {
    position: absolute; left: 0; right: 0; top: 796px; text-align: center;
    font-family: "Montserrat", sans-serif; font-weight: 700; font-size: 17px; color: var(--white);
  }
</style>
</head>
<body>
<main class="canvas">
  <section class="label" aria-label="RIVO BREW non alcoholic beer can label">
    <div class="side-pattern left" role="img" aria-label="Silver side panel with fine line pattern"></div>
    <div class="side-pattern right" role="img" aria-label="Silver side panel with fine line pattern"></div>
    <div class="red-panel" role="img" aria-label="Red central panel with fine wave line pattern"></div>

    <svg class="brand-frame" viewBox="0 0 360 220" aria-hidden="true">
      <polygon points="20,60 60,28 180,2 300,28 340,60 340,160 300,192 180,218 60,192 20,160" fill="var(--white)"/>
      <polygon points="28,64 64,34 180,10 296,34 332,64 332,156 296,186 180,210 64,186 28,156" fill="var(--blue)"/>
      <polygon points="36,68 68,42 180,20 292,42 324,68 324,152 292,178 180,200 68,178 36,152" fill="none" stroke="var(--gold)" stroke-width="2.5"/>
    </svg>

    <div class="brand-badge"><span>RIVO BREW</span></div>
    <div class="flourish" role="img" aria-label="Gold scroll ornament"></div>
    <div class="laurel left" role="img" aria-label="Gold laurel branch"></div>
    <div class="laurel right" role="img" aria-label="Gold laurel branch"></div>
    <div class="brand-name">RIVO BREW</div>
    <div class="brand-sub">Premium</div>

    <svg class="alc-band" viewBox="0 0 276 210" aria-hidden="true">
      <polygon points="0,50 276,0 276,150 0,210" fill="var(--blue)"/>
    </svg>
    <div class="alc-mark">
      <span class="alc-figure">0.0</span>
      <span class="alc-side">
        <span class="alc-percent">%</span>
        <span class="alc-unit">ALC.</span>
      </span>
    </div>

    <div class="variant">
      <p class="variant-tier">PREMIUM</p>
      <p class="variant-name">ORIGINAL</p>
      <p class="variant-type">NON ALCOHOLIC BEER</p>
      <div class="variant-rule"></div>
    </div>

    <p class="volume">500ml</p>
  </section>
</main>
</body>
</html>
```